Logo and business card

RVK Financial Solutions - Branding & Image Project

There will be 3 companies in our group. We want a similar Branding look & feel for all 3. The first company is DLW Financial which is already established, and I have included samples of the branding.

The goal for this design project is to create the corporate branding for RVK Financial Solutions which is the second company in the group.

Please use the same colours and fonts that we use at DLW Financial but the logo must be different. The final design should communicate financial safety and growth. Our typical clients are 40+ years and financially conservative.

Can you create a sample version using the dark green in the attached image.

We will need print resolution files and low res file for email, web etc.

The main printed outputs we need are – see separate attachment for examples;
Business Card 2 sided
Web logo

We’ll then need the following
Letterhead & follow on sheets
Envelopes C5 2 sided & C4 2 sided
Compliment Slips

```html
<!DOCTYPE html>
<html lang="en">
<head>
<meta charset="utf-8">
<title>RVK Financial Solutions – Business Card</title>
<link rel="stylesheet" href="https://fonts.googleapis.com/css2?family=EB+Garamond:wght@400;500&family=Playfair+Display:wght@500&display=swap">
<style>
  :root {
    --page-bg: #ecebe7;
    --card-bg: #fafaf8;
    --ink: #1f1f1f;
    --ink-soft: #3a3a3a;
    --gold: #c9a227;
  }
  * { box-sizing: border-box; margin: 0; padding: 0; }
  html, body { width: 1200px; height: 900px; overflow: hidden; }
  body {
    background: var(--page-bg);
    display: flex;
    align-items: center;
    justify-content: center;
    gap: 40px;
    font-family: "EB Garamond", Georgia, serif;
    color: var(--ink);
  }
  .card {
    position: relative;
    width: 540px;
    height: 310px;
    background: var(--card-bg);
    box-shadow: 0 6px 18px rgba(0,0,0,0.12);
  }

  /* Front */
  .card-front .brand {
    position: absolute;
    left: 140px;
    top: 92px;
    display: flex;
    align-items: center;
    gap: 14px;
  }
  .brand-square {
    width: 44px;
    height: 44px;
    border: 1.5px solid var(--gold);
  }
  .brand-name {
    font-size: 27px;
    font-weight: 400;
    line-height: 1.05;
    color: var(--ink-soft);
  }
  .card-front .rule {
    position: absolute;
    left: 110px;
    right: 110px;
    top: 184px;
    height: 1px;
    background: var(--gold);
  }
  .legal {
    position: absolute;
    left: 0;
    right: 0;
    top: 196px;
    text-align: center;
    font-size: 11.5px;
    line-height: 1.5;
    color: var(--ink-soft);
  }

  /* Back */
  .person-name {
    position: absolute;
    left: 48px;
    top: 44px;
    font-family: "Playfair Display", Georgia, serif;
    font-weight: 500;
    font-size: 28px;
    color: var(--ink);
  }
  .person-title {
    position: absolute;
    left: 50px;
    top: 84px;
    font-size: 13px;
    color: var(--gold);
  }
  .contact-list {
    position: absolute;
    left: 50px;
    top: 122px;
    display: grid;
    grid-template-columns: 90px 14px auto;
    row-gap: 2px;
    font-size: 12.5px;
    color: var(--ink-soft);
  }
  .card-back .rule {
    position: absolute;
    left: 50px;
    right: 110px;
    top: 222px;
    height: 1px;
    background: var(--gold);
  }
  .address {
    position: absolute;
    left: 50px;
    top: 234px;
    font-style: normal;
    font-size: 12px;
    line-height: 1.45;
    color: var(--ink-soft);
  }
  .card-back .brand-square {
    position: absolute;
    right: 52px;
    top: 54px;
  }
</style>
</head>
<body>
  <section class="card card-front" aria-label="Business card front">
    <div class="brand">
      <span class="brand-square"></span>
      <span class="brand-name">RVK Financial<br>Solutions</span>
    </div>
    <div class="rule"></div>
    <p class="legal">
      RVK Financial Solutions Limited is authorised and regulated by the Financial Standards Authority<br>
      Authority reference 583120<br>
      Registered in England and Wales No. 609354
    </p>
  </section>

  <section class="card card-back" aria-label="Business card back">
    <h1 class="person-name">Harriet Lomax</h1>
    <p class="person-title">Senior Wealth Adviser</p>
    <div class="contact-list">
      <span>Office</span><span>:</span><span>01632 960418</span>
      <span>Mobile</span><span>:</span><span>07700 900274</span>
      <span>E-Mail</span><span>:</span><span>harriet.lomax@rvkfs.co.uk</span>
      <span>Website</span><span>:</span><span>www.rvkfs.co.uk</span>
    </div>
    <div class="rule"></div>
    <address class="address">
      The Old Granary, Unit 4 Mill Lane Business Park<br>
      Orchard Road, Ashcombe<br>
      Westbury, Wilts, BA9 4QT
    </address>
    <span class="brand-square"></span>
  </section>
</body>
</html>
```